Mesh Banner Design for Business Premises

We require the design of a large mesh banner to be installed across the front fence of our warehouse. The banner should prominently feature our existing Trelborn logo and brand colours (yellow, white, and black) and be designed to be highly visible from the road.

The overall aesthetic should be strong, masculine, and industrial, reflecting the nature of the scaffolding and construction industry. The background should be predominantly black, with our branding incorporated in yellow and white for strong contrast and readability.

The banner should clearly communicate the full scope of services we provide, including:

Scaffold Design
Scaffold Engineering
Scaffold Installation / Erection
Scaffold Dismantling

It should also indicate the types of projects and clients we service, including:

Commercial
Industrial
Residential
Civil

The design should feel bold and professional, with a construction-oriented style that aligns with the scaffolding industry. It should be clean, impactful, and easy to read from a distance, ensuring passing traffic can quickly understand our services.

Where possible, subtle industrial or structural design elements (such as scaffold components, steel textures, or linework) may be incorporated into the background to reinforce the industry theme while keeping the layout uncluttered.

The final design will be produced as a large-format mesh banner for outdoor installation, so it should be created with this application and viewing distance in mind.

```html
<!DOCTYPE html>
<html lang="en">
<head>
<meta charset="utf-8">
<title>Trelborn Mesh Banner</title>
<link rel="stylesheet" href="https://fonts.googleapis.com/css2?family=Questrial&family=Mulish:wght@800&family=Montserrat:wght@600;700&display=swap">
<style>
  :root {
    --stage: #bdbdbd;
    --banner-black: #231f20;
    --brand-yellow: #f6a623;
    --white: #ffffff;
    --line-white: rgba(255, 255, 255, 0.22);
  }
  html, body {
    margin: 0;
    padding: 0;
    width: 1200px;
    height: 403px;
    overflow: hidden;
    background: var(--stage);
  }
  .banner {
    position: absolute;
    left: 97px;
    top: 69px;
    width: 1008px;
    height: 257px;
    background: var(--banner-black);
    overflow: hidden;
  }
  .heading {
    position: absolute;
    margin: 0;
    font-family: "Mulish", sans-serif;
    font-weight: 800;
    font-size: 18px;
    line-height: 21.5px;
    color: var(--brand-yellow);
    letter-spacing: 0.2px;
  }
  .services-heading { left: 45px; top: 43px; }
  .projects-heading { left: 755px; top: 39px; }
  .checklist {
    position: absolute;
    margin: 0;
    padding: 0;
    list-style: none;
    font-family: "Questrial", sans-serif;
    font-size: 19px;
    line-height: 22.4px;
    color: var(--white);
  }
  .checklist li {
    position: relative;
    padding-left: 18px;
  }
  .checklist li::before {
    content: "\2713";
    position: absolute;
    left: 0;
    top: 1px;
    color: var(--brand-yellow);
    font-size: 17px;
  }
  .services-list { left: 45px; top: 88px; width: 220px; }
  .services-list li { padding-left: 17px; }
  .projects-list { left: 788px; top: 108px; }
  .structure-art {
    position: absolute;
    left: 234px;
    top: 134px;
    width: 535px;
    height: 115px;
    background:
      linear-gradient(180deg, rgba(255,255,255,0.10) 0%, rgba(255,255,255,0.20) 60%, rgba(255,255,255,0.06) 100%);
    clip-path: polygon(0 8%, 20% 0, 45% 100%, 55% 100%, 80% 0, 100% 8%, 92% 100%, 8% 100%);
  }
  .brand-name {
    position: absolute;
    left: 0;
    width: 1008px;
    top: 96px;
    margin: 0;
    text-align: center;
    font-family: "Montserrat", sans-serif;
    font-weight: 600;
    font-size: 17px;
    letter-spacing: 12px;
    text-indent: 12px;
    color: var(--white);
  }
  .phone {
    position: absolute;
    left: 0;
    width: 1008px;
    top: 126px;
    margin: 0;
    text-align: center;
    font-family: "Montserrat", sans-serif;
    font-weight: 700;
    font-size: 31px;
    letter-spacing: -0.5px;
    color: var(--white);
  }
</style>
</head>
<body>
  <main class="banner">
    <h2 class="heading services-heading">Services we provide</h2>
    <ul class="checklist services-list">
      <li>Scaffold Design</li>
      <li>Scaffold<br>Engineering</li>
      <li>Scaffold<br>Installation / Erection</li>
      <li>Scaffold Dismantling</li>
    </ul>

    <div class="structure-art" role="img" aria-label="White linework drawing of a winged steel roof structure with scaffolding"></div>

    <h1 class="brand-name">TRELBORN</h1>
    <p class="phone">1300 8 BUILD</p>

    <h2 class="heading projects-heading">Types of projects<br>and clients we service</h2>
    <ul class="checklist projects-list">
      <li>Commercial</li>
      <li>Industrial</li>
      <li>Residential</li>
      <li>Civil</li>
    </ul>
  </main>
</body>
</html>
```